Vesta Realty Recruiting Flyer

I Need a flyer design to recruit real estate agents to join my company. we need the focal point to be our new commission split which is 100% Commission No Monthly Fee $450.00 Transaction Fee with $4500.00 Annual Cap. what we offer:
24/7 Office Access
Free Online CE and PLE
Free Printing, Scanning, and Copies
Free E & O Insurance
Free 1,000 Business Cards
Free Lockbox Usage
Free Sign Usage
Free Marketing Material Templates
Licensed: D.C., Maryland, Virginia, and Indiana I have attached one of our competitors flyers as well as our company logo.

Reason: Need Company Info in flyer Vesta Realty 2847-B Fernmont Lane Annandale, VA 22917 703-491-2786 www.vestarealtyhub.net info@vestarealtyhub.net Please add Homebroker Logo as well as Fair Dwelling Access logo on the bottom of add... 1 sided 8 by 11

```html
<!DOCTYPE html>
<html lang="en">
<head>
<meta charset="utf-8">
<title>Vesta Realty – Recruiting Real Estate Agents</title>
<link href="https://fonts.googleapis.com/css2?family=Montserrat:wght@500;600;700;800&display=swap" rel="stylesheet">
<style>
  :root {
    --navy: #1f2d4f;
    --navy-deep: #131d36;
    --blue: #2a4a86;
    --orange: #f49a1c;
    --orange-light: #f8b133;
    --paper: #f3f4f6;
    --mist: #e2e5ea;
    --white: #ffffff;
    --soft-white: #d9dfeb;
  }
  * { margin: 0; padding: 0; box-sizing: border-box; }
  html, body { width: 851px; height: 1200px; overflow: hidden; background: var(--white); }
  .flyer {
    position: relative;
    width: 851px;
    height: 1200px;
    overflow: hidden;
    font-family: "Montserrat", Arial, sans-serif;
    background: linear-gradient(180deg, var(--white) 0%, var(--paper) 60%, var(--mist) 100%);
  }
  .backdrop { position: absolute; inset: 0; }
  .skyline {
    position: absolute;
    right: 0; top: 560px;
    width: 420px; height: 545px;
    background: linear-gradient(180deg, rgba(200,205,214,0) 0%, rgba(190,196,206,0.55) 60%, rgba(175,182,194,0.75) 100%);
  }
  .brand {
    position: absolute;
    top: 62px; right: 40px;
    display: flex; align-items: center; gap: 12px;
  }
  .brand-mark { width: 32px; height: 32px; background: var(--navy); }
  .brand-name { font-size: 28px; font-weight: 700; color: var(--navy); letter-spacing: 0.5px; }

  .headline { position: absolute; top: 190px; left: 0; width: 851px; text-align: center; color: var(--navy); }
  .headline-main { font-size: 70px; font-weight: 600; letter-spacing: 1px; line-height: 1; }
  .headline-sub { margin-top: 16px; font-size: 31px; font-weight: 600; letter-spacing: 1px; line-height: 1; }

  .badge { position: absolute; left: 90px; top: 318px; width: 246px; height: 246px; }
  .badge-text {
    position: absolute; inset: 0;
    display: flex; flex-direction: column; align-items: center; justify-content: center;
    color: var(--white); transform: rotate(-14deg);
  }
  .badge-percent { font-size: 58px; font-weight: 800; line-height: 1; }
  .badge-label { font-size: 23px; font-weight: 700; letter-spacing: 0.5px; margin-top: 4px; }

  .offer-terms { position: absolute; left: 397px; top: 350px; color: var(--blue); }
  .terms-lead { font-size: 34px; font-weight: 700; color: var(--orange); line-height: 1.1; }
  .terms-detail { margin-top: 10px; font-size: 20px; font-weight: 500; line-height: 1.65; }

  .benefits { position: absolute; left: 104px; top: 650px; color: var(--white); }
  .benefits-title { font-size: 60px; font-weight: 700; color: var(--orange-light); line-height: 1.1; letter-spacing: 1px; margin-left: 22px; }
  .benefit-list { list-style: none; margin-top: 18px; }
  .benefit-list li {
    display: flex; align-items: center; gap: 12px;
    font-size: 23px; font-weight: 500; line-height: 1; height: 37px;
  }
  .tick { width: 22px; height: 22px; flex: none; }

  .company-info {
    position: absolute; left: 0; bottom: 0;
    width: 851px; height: 92px;
    background: var(--navy-deep);
    display: flex; align-items: center; justify-content: space-between;
    padding: 0 40px;
    color: var(--soft-white);
    font-size: 14px; font-weight: 500; line-height: 1.55;
  }
  .company-name { color: var(--orange-light); font-weight: 700; font-size: 15px; }
  .licensed { color: var(--white); font-weight: 600; }
  .marks { display: flex; gap: 14px; align-items: center; }
  .mark-round { width: 44px; height: 44px; border-radius: 50%; background: var(--soft-white); }
  .mark-square { width: 44px; height: 44px; background: var(--soft-white); }
</style>
</head>
<body>
<main class="flyer">
  <svg class="backdrop" width="851" height="1200" viewBox="0 0 851 1200" aria-hidden="true">
    <defs>
      <linearGradient id="panelFill" x1="0" y1="0" x2="1" y2="1">
        <stop offset="0" stop-color="#2c4c88"/>
        <stop offset="0.55" stop-color="#1d3263"/>
        <stop offset="1" stop-color="#131f3c"/>
      </linearGradient>
    </defs>
    <polygon points="420,0 851,0 851,330 620,560" fill="#eceef2"/>
    <polygon points="0,330 260,600 0,800" fill="#e9ebef"/>
    <polygon points="0,620 520,570 708,620 708,1200 0,1200" fill="url(#panelFill)"/>
  </svg>

  <div class="skyline" role="img" aria-label="Faint city skyline of office towers"></div>

  <div class="brand">
    <span class="brand-mark"></span>
    <span class="brand-name">Vesta Realty</span>
  </div>

  <header class="headline">
    <h1 class="headline-main">RECRUITING</h1>
    <p class="headline-sub">REAL ESTATE AGENTS</p>
  </header>

  <div class="badge">
    <svg width="246" height="246" viewBox="0 0 246 246" aria-hidden="true">
      <g fill="var(--orange)" transform="translate(123 123)">
        <rect x="-86" y="-86" width="172" height="172"/>
        <rect x="-86" y="-86" width="172" height="172" transform="rotate(22.5)"/>
        <rect x="-86" y="-86" width="172" height="172" transform="rotate(45)"/>
        <rect x="-86" y="-86" width="172" height="172" transform="rotate(67.5)"/>
      </g>
      <circle cx="123" cy="123" r="96" fill="none" stroke="#ffffff" stroke-width="2" opacity="0.6"/>
    </svg>
    <div class="badge-text">
      <span class="badge-percent">100%</span>
      <span class="badge-label">COMMISSION</span>
    </div>
  </div>

  <section class="offer-terms">
    <p class="terms-lead">NO MONTHLY FEE</p>
    <p class="terms-detail">$450.00 TRANSACTION FEE<br>WITH $4500.00 ANNUAL CAP</p>
  </section>

  <section class="benefits">
    <h2 class="benefits-title">WHAT WE<br>OFFER:</h2>
    <ul class="benefit-list">
      <li><svg class="tick" viewBox="0 0 24 24" aria-hidden="true"><path d="M3 13l6 6L21 5" fill="none" stroke="var(--orange)" stroke-width="4" stroke-linecap="round" stroke-linejoin="round"/></svg>24/7 Office Access</li>
      <li><svg class="tick" viewBox="0 0 24 24" aria-hidden="true"><path d="M3 13l6 6L21 5" fill="none" stroke="var(--orange)" stroke-width="4" stroke-linecap="round" stroke-linejoin="round"/></svg>Free Online CE and PLE</li>
      <li><svg class="tick" viewBox="0 0 24 24" aria-hidden="true"><path d="M3 13l6 6L21 5" fill="none" stroke="var(--orange)" stroke-width="4" stroke-linecap="round" stroke-linejoin="round"/></svg>Free Printing, Scanning, and Copies</li>
      <li><svg class="tick" viewBox="0 0 24 24" aria-hidden="true"><path d="M3 13l6 6L21 5" fill="none" stroke="var(--orange)" stroke-width="4" stroke-linecap="round" stroke-linejoin="round"/></svg>Free E &amp; O Insurance</li>
      <li><svg class="tick" viewBox="0 0 24 24" aria-hidden="true"><path d="M3 13l6 6L21 5" fill="none" stroke="var(--orange)" stroke-width="4" stroke-linecap="round" stroke-linejoin="round"/></svg>Free 1,000 Business Cards</li>
      <li><svg class="tick" viewBox="0 0 24 24" aria-hidden="true"><path d="M3 13l6 6L21 5" fill="none" stroke="var(--orange)" stroke-width="4" stroke-linecap="round" stroke-linejoin="round"/></svg>Free Lockbox Usage</li>
      <li><svg class="tick" viewBox="0 0 24 24" aria-hidden="true"><path d="M3 13l6 6L21 5" fill="none" stroke="var(--orange)" stroke-width="4" stroke-linecap="round" stroke-linejoin="round"/></svg>Free Sign Usage</li>
      <li><svg class="tick" viewBox="0 0 24 24" aria-hidden="true"><path d="M3 13l6 6L21 5" fill="none" stroke="var(--orange)" stroke-width="4" stroke-linecap="round" stroke-linejoin="round"/></svg>Free Marketing Material Templates</li>
    </ul>
  </section>

  <footer class="company-info">
    <div class="company-address">
      <p class="company-name">Vesta Realty</p>
      <p>2847-B Fernmont Lane, Annandale, VA 22917</p>
      <p class="licensed">Licensed: D.C., Maryland, Virginia, and Indiana</p>
    </div>
    <div class="company-contact">
      <p>703-491-2786</p>
      <p>www.vestarealtyhub.net</p>
      <p>info@vestarealtyhub.net</p>
    </div>
    <div class="marks">
      <span class="mark-round" role="img" aria-label="Homebroker membership badge"></span>
      <span class="mark-square" role="img" aria-label="Fair Dwelling Access badge"></span>
    </div>
  </footer>
</main>
</body>
</html>
```